Business Card Design Project

Looking for a business card that our customers will remember. We are a high end Travel Agency.
Need a re-memorable classy business card.
Both sides full color.
Must have the following details.
Voyage Harbor Logo (see attached)
4B Wattle Lane
Penhurst Sydney NSW 2241
Phone: 02 9471 3652
Fax: 02 9563 4417
sales@voyageharbor-example.com.au
Consultant Name
Anything else you think we need

```html
<!DOCTYPE html>
<html lang="en">
<head>
<meta charset="utf-8">
<title>Voyage Harbor – Business Card</title>
<link rel="stylesheet" href="https://fonts.googleapis.com/css2?family=Exo+2:wght@400;600;700&display=swap">
<style>
  :root {
    --backdrop: #2b2b2d;
    --harbor-blue: #1f5a7f;
    --sun-yellow: #f6c41a;
    --sun-yellow-deep: #d9a80e;
    --paper: #ffffff;
    --ink-navy: #1d3a5c;
    --text-light: #ffffff;
  }
  * { box-sizing: border-box; margin: 0; padding: 0; }
  html, body {
    width: 1200px; height: 900px; overflow: hidden;
    background: var(--backdrop);
    font-family: "Exo 2", sans-serif;
  }
  .canvas {
    position: relative; width: 1200px; height: 900px;
    display: flex; flex-direction: column; align-items: center; justify-content: center;
    gap: 40px;
  }
  .card {
    position: relative; width: 640px; height: 390px; overflow: hidden;
    background: var(--harbor-blue);
    box-shadow: 0 10px 30px rgba(0,0,0,.45);
  }
  .pattern-band {
    position: absolute; left: 0; top: 0; width: 100%; height: 44%;
    background: linear-gradient(180deg, var(--sun-yellow) 0%, var(--sun-yellow-deep) 100%);
  }
  .logo-strip {
    position: absolute; top: 0; height: 100%; width: 118px;
    background: var(--paper);
    display: flex; align-items: center; justify-content: center;
  }
  .card--front .logo-strip { left: 260px; }
  .card--back .logo-strip { left: 64px; }
  .brand {
    display: flex; align-items: center; gap: 12px;
    transform: rotate(-90deg); white-space: nowrap;
  }
  .brand-mark { width: 12px; height: 12px; border-radius: 50%; background: var(--ink-navy); }
  .brand-name {
    font-weight: 600; font-size: 30px; letter-spacing: 2px;
    color: var(--ink-navy); text-transform: uppercase;
  }
  .holder {
    position: absolute; right: 0; top: 186px;
    display: flex; align-items: flex-start; gap: 10px;
  }
  .holder-text { text-align: right; }
  .holder-name {
    color: var(--sun-yellow); font-weight: 700; font-size: 17px;
    letter-spacing: 1px; text-transform: uppercase;
  }
  .holder-role { color: var(--text-light); font-size: 14px; margin-top: 2px; }
  .holder-tab { width: 12px; height: 26px; background: var(--sun-yellow); }
  .contact {
    position: absolute; left: 212px; top: 254px; right: 24px;
    display: grid; grid-template-columns: 190px 1fr; column-gap: 22px;
    color: var(--text-light); font-size: 14.5px; line-height: 1.35;
  }
  .address { grid-column: 1; margin-bottom: 18px; }
  .phones { grid-column: 1; }
  .online { grid-column: 2; grid-row: 1 / span 2; align-self: end; }
  .label { color: var(--sun-yellow); font-weight: 600; margin-right: 4px; }
</style>
</head>
<body>
<main class="canvas">
  <section class="card card--front" aria-label="Card front">
    <div class="pattern-band" role="img" aria-label="Yellow typographic pattern of travel words: fares, cruises, hotels, holidays, insurance, cars"></div>
    <div class="logo-strip">
      <div class="brand"><span class="brand-mark"></span><span class="brand-name">Voyage Harbor</span></div>
    </div>
  </section>

  <section class="card card--back" aria-label="Card back">
    <div class="pattern-band" role="img" aria-label="Yellow typographic pattern of travel words: fares, cruises, hotels, holidays, insurance, cars"></div>
    <div class="logo-strip">
      <div class="brand"><span class="brand-mark"></span><span class="brand-name">Voyage Harbor</span></div>
    </div>
    <div class="holder">
      <div class="holder-text">
        <p class="holder-name">Daniel Marsh</p>
        <p class="holder-role">Manager</p>
      </div>
      <span class="holder-tab"></span>
    </div>
    <div class="contact">
      <p class="address">4B Wattle Lane<br>Penhurst Sydney NSW 2241</p>
      <p class="phones"><span class="label">P:</span>02 9471 3652<br><span class="label">F:</span>02 9563 4417</p>
      <p class="online"><span class="label">E:</span>sales@voyageharbor-example.com.au<br><span class="label">W:</span>www.voyageharbor-example.com.au</p>
    </div>
  </section>
</main>
</body>
</html>
```